Business & Good Life in perfect harmony

Our company is engage in event planning & services , we have Convention center ideal for seminars, retreats,conventions, conferences or even concerts & also offers lodging facilities particularly of "ON - LINE ROOM RESERVATIONS /ACCOMMODATIONS "
Also we have Clubhouse & restobar , an elegant venue ideal for weddings, birthday celebration, parties & other memorable gatherings, as well as sports activities.
Target Market(s)
Travellers
Event Organizers
Conference / seminar Coordinators
Industry/Entity Type
Event Planning
Contact Information for Business Card
Lia B. Morendo , Sales & Operation Manager
Stonebrook Business & Convention Center Corp.
/ Stonebrook Clubhouse & Restobar
Contact #s : 082-5193068 ; 0917 4362580
Website : www. stonebrookvenue.example
Email add : stonebrook.lia.venue@mailbox.example
stonebrook.venue@postbox.example
Facebook : Stonebrook Venue
Font styles to use
Look and feel
Each slider illustrates characteristics of the customer's brand and the style your logo design should communicate.

```html
<!DOCTYPE html>
<html lang="en">
<head>
<meta charset="utf-8">
<title>Stonebrook Business Card</title>
<link rel="stylesheet" href="https://fonts.googleapis.com/css2?family=Noto+Serif:ital,wght@0,400;1,400&family=Pinyon+Script&display=swap">
<style>
  :root {
    --backdrop: #eef0f1;
    --card-white: #ffffff;
    --brand-green: #9dcb41;
    --accent-teal: #1aa89a;
    --text-grey: #6f7b7a;
    --on-green: #ffffff;
  }
  * { margin: 0; padding: 0; box-sizing: border-box; }
  html, body {
    width: 1200px;
    height: 900px;
    overflow: hidden;
    background: var(--backdrop);
    font-family: "Noto Serif", Georgia, serif;
  }
  .canvas { position: relative; width: 1200px; height: 900px; }
  .card {
    position: absolute;
    top: 306px;
    width: 504px;
    height: 288px;
  }
  .card--front { left: 80px; background: var(--card-white); }
  .card--back {
    left: 616px;
    background: var(--brand-green);
    display: flex;
    align-items: center;
    justify-content: center;
  }
  .front__phones {
    position: absolute;
    top: 32px;
    left: 0; right: 0;
    text-align: center;
    color: var(--accent-teal);
    font-size: 14px;
    letter-spacing: 0.3px;
  }
  .front__phones .divider { margin: 0 10px; }
  .front__identity {
    position: absolute;
    top: 98px;
    left: 0; right: 0;
    display: flex;
    justify-content: center;
    align-items: baseline;
    gap: 12px;
  }
  .identity__name {
    font-family: "Pinyon Script", cursive;
    color: var(--accent-teal);
    font-size: 26px;
  }
  .identity__title {
    font-style: italic;
    color: var(--text-grey);
    font-size: 13.5px;
  }
  .front__rule {
    position: absolute;
    top: 136px;
    left: 60px;
    width: 386px;
    height: 2px;
    background: var(--brand-green);
  }
  .front__companies {
    position: absolute;
    top: 146px;
    left: 0; right: 0;
    text-align: center;
    font-style: italic;
    color: var(--text-grey);
    font-size: 11.5px;
    line-height: 17px;
  }
  .front__contacts {
    position: absolute;
    top: 222px;
    left: 0; right: 0;
    text-align: center;
    color: var(--accent-teal);
    font-size: 11.5px;
    line-height: 15px;
  }
  .contacts__label { font-style: italic; }
  .contacts__sep { margin: 0 7px; }
  .back__website {
    color: var(--on-green);
    font-style: italic;
    font-size: 16.5px;
    letter-spacing: 0.3px;
  }
</style>
</head>
<body>
  <main class="canvas">
    <section class="card card--front" aria-label="Business card front">
      <p class="front__phones">082-519-306-8<span class="divider">|</span>091-743-625-80</p>
      <div class="front__identity">
        <span class="identity__name">Lia B. Morendo</span>
        <span class="identity__title">Sales &amp; Operation Manager</span>
      </div>
      <div class="front__rule"></div>
      <p class="front__companies">
        Stonebrook Business &amp; Convention Center Corp.<br>
        Stonebrook Clubhouse &amp; Restobar
      </p>
      <p class="front__contacts">
        <span class="contacts__label">Email:</span> stonebrook.lia.venue@mailbox.example<span class="contacts__sep">|</span><br>
        stonebrook.venue@postbox.example<span class="contacts__sep">|</span><span class="contacts__label">Facebook:</span> Stonebrook Venue
      </p>
    </section>
    <section class="card card--back" aria-label="Business card back">
      <p class="back__website">www.stonebrookvenue.example</p>
    </section>
  </main>
</body>
</html>
```